Packaging Design New Cosmetics Range

Small Establish online Beauty company is expanding it's product range into Serums, Sprays and Creams . We are looking for a new fresh packaging design for this launch.
We only use products that are Organic , Not Tested on Animals and Natural products
We would be interested in viewing a White Design , Black design and a designer choice of colors .
First Products are
Rose Water in 100ml glass bottle with box
and a set of 3 Face Serums Vit C , Retinol and Hyaluronic in 30ml Glass bottle = Box
Scrubs and creams will launch later in Q1 2020 however would like a similar feel across all products
Target Market(s)
SEA / US Markets
Industry/Entity Type
Cosmetics
Colors
Designer to choose colors to be used in the design.
Requirements
Must have
- Space Allocated for Product Use and Bar Codes on Box
Nice to have
- Organic , Not tested on animal Logo's

```html
<!DOCTYPE html>
<html lang="en">
<head>
<meta charset="utf-8">
<title>Lunava Rose Water Label</title>
<link rel="stylesheet" href="https://fonts.googleapis.com/css2?family=Archivo+Black&family=Comfortaa:wght@400&family=Kaushan+Script&display=swap">
<style>
  :root {
    --teal: #14a88f;
    --white: #ffffff;
    --rose-red: #7d1416;
    --ink: #3a3a3a;
    --backdrop: #ececec;
    --petal-light: #f7c9d2;
    --petal-deep: #e98ea0;
    --leaf: #9fc7a4;
  }
  html, body {
    margin: 0;
    padding: 0;
    width: 1200px;
    height: 2535px;
    overflow: hidden;
    background: var(--backdrop);
  }
  .label {
    position: absolute;
    left: 106px;
    top: 766px;
    width: 988px;
    height: 1002px;
    background: var(--teal);
    overflow: hidden;
  }
  .label__rule {
    position: absolute;
    left: 39px;
    right: 19px;
    top: 42px;
    bottom: 47px;
    border: 3px solid var(--white);
  }
  .label__panel {
    position: absolute;
    left: 88px;
    right: 39px;
    top: 85px;
    bottom: 81px;
    background: var(--white);
  }
  .label__roses {
    position: absolute;
    left: 0;
    top: 0;
    width: 500px;
    height: 414px;
    border-radius: 0 0 62% 0 / 0 0 58% 0;
    background: radial-gradient(circle at 35% 45%, var(--petal-light), var(--petal-deep) 72%, rgba(233,142,160,0.85) 100%);
  }
  .label__leaves {
    position: absolute;
    left: 0;
    top: 363px;
    width: 164px;
    height: 407px;
    border-radius: 0 0 80% 0 / 0 0 60% 0;
    background: linear-gradient(180deg, var(--leaf), rgba(159,199,164,0.35));
  }
  .brand {
    position: absolute;
    left: 505px;
    width: 400px;
    top: 270px;
    text-align: center;
    font-family: "Comfortaa", sans-serif;
    font-weight: 400;
    font-size: 100px;
    line-height: 1;
    color: var(--teal);
  }
  .product-name {
    position: absolute;
    right: 157px;
    top: 405px;
    margin: 0;
    font-family: "Archivo Black", sans-serif;
    font-style: italic;
    font-weight: 400;
    font-variant: small-caps;
    font-size: 262px;
    line-height: 1;
    letter-spacing: 2px;
    color: var(--rose-red);
    white-space: nowrap;
  }
  .product-type {
    position: absolute;
    right: 157px;
    top: 640px;
    font-family: "Kaushan Script", cursive;
    font-size: 92px;
    line-height: 1;
    color: var(--ink);
  }
  .volume-tab {
    position: absolute;
    left: 366px;
    top: 811px;
    width: 254px;
    height: 110px;
    border-radius: 127px 127px 0 0;
    background: var(--teal);
    display: flex;
    align-items: center;
    justify-content: center;
    padding-top: 16px;
    box-sizing: border-box;
    font-family: "Kaushan Script", cursive;
    font-size: 48px;
    line-height: 1;
    color: var(--white);
  }
</style>
</head>
<body>
  <main class="label">
    <div class="label__rule"></div>
    <div class="label__panel"></div>
    <div class="label__roses" role="img" aria-label="Watercolour pink roses with green leaves"></div>
    <div class="label__leaves" role="img" aria-label="Watercolour eucalyptus leaves trailing down the left edge"></div>
    <div class="brand">Lunava</div>
    <h1 class="product-name">Rose</h1>
    <div class="product-type">water</div>
    <div class="volume-tab">100ml</div>
  </main>
</body>
</html>
```